Skin care line needs a LABEL designed!

Fernlight Skin Care... An EARTHY modern boho chic skin care line needs a label designed. It is called Fernlight because there are healing crystals in the product. Holistic, yoga feel, Earthy, feminine.

This contest is for 1 cleanser label- 2 different versions:

Gel Cleanser
Milk Cleanser

Label Size: 4.8125 x 4.8125 in

Winner will be selected to do the labels for:
Toner (5 Versions)
Serum (5 Versions)
Moisturizer (3 Versions)
Sample Label and packaging

Please be prepared to quote a price for the additional labels listed.

Inspiring Brands: **Corvella Studio**, Marigrove Organics, Tessa Wren, Halvenmoor beauty product brands,

Feel free to separate the logo symbol and use it somewhere else in the design.

Target Market(s)

Women ages 30-60

Industry/Entity Type

Skin Care Product

Requirements
Must have
• Tag Line: Inner Peace- Outer Beauty
• Area for ingredients
• Earthy feel
• Large STEP 1 on the front of packaging
• Disclaimer:
• Note: Metaphysical descriptions and healing properties of crystals are not meant to replace medical advice or treat any condition. For external use only.
Nice to have
• www.fernlight-skincare.example
Should not have
• Multiple Colors

```html
<!DOCTYPE html>
<html lang="en">
<head>
<meta charset="utf-8">
<title>Fernlight Skin Care – Cleanser Gel Labels</title>
<link href="https://fonts.googleapis.com/css2?family=Oswald:wght@300&family=Poppins:wght@600&family=Great+Vibes&family=Arimo&display=swap" rel="stylesheet">
<style>
  :root {
    --teal: #00968a;
    --teal-deep: #138f84;
    --teal-bright: #5ce1d6;
    --teal-pale: #cbe6e4;
    --paper: #ffffff;
    --pattern-light: #f0efef;
    --night: #1a1719;
    --plum: #2e1628;
    --stage: #ececec;
    --ink-soft: #b9b3b8;
  }
  * { margin: 0; padding: 0; box-sizing: border-box; }
  html, body { width: 1200px; height: 867px; overflow: hidden; }
  body {
    background: var(--stage);
    font-family: "Arimo", Arial, sans-serif;
    position: relative;
  }
  .label {
    position: absolute;
    width: 494px;
    height: 480px;
    background: var(--paper);
    overflow: hidden;
  }
  .label--light { left: 64px; top: 164px; }
  .label--dark {
    left: 626px; top: 162px; height: 488px;
    background: linear-gradient(90deg, var(--night) 0%, var(--night) 55%, var(--plum) 60%, var(--plum) 100%);
  }
  .pattern {
    position: absolute;
    left: 20px; top: 40px; width: 474px; height: 420px;
  }
  .label--light .pattern {
    background: radial-gradient(ellipse at 30% 55%, var(--pattern-light) 0%, rgba(240,239,239,0.6) 45%, rgba(255,255,255,0) 75%),
                radial-gradient(ellipse at 85% 55%, var(--pattern-light) 0%, rgba(255,255,255,0) 60%);
  }
  .label--dark .pattern {
    background: radial-gradient(ellipse at 30% 55%, rgba(120,110,118,0.45) 0%, rgba(60,55,60,0.2) 50%, rgba(0,0,0,0) 75%),
                radial-gradient(ellipse at 85% 60%, rgba(150,110,140,0.45) 0%, rgba(0,0,0,0) 60%);
  }
  .band { position: absolute; left: 0; width: 100%; background: var(--teal); }
  .band--top { top: 0; height: 25px; }
  .band--bottom { top: 466px; height: 12px; }
  .label--dark .band--bottom { top: 468px; }
  .tagline {
    position: absolute; right: 45px; top: 3px;
    font-family: "Oswald", "Arial Narrow", sans-serif; font-weight: 300;
    font-size: 13.5px; color: var(--paper); letter-spacing: 0.1px;
  }
  .note-box {
    position: absolute; left: 32px; top: 42px; width: 164px; height: 91px;
    border: 2px solid #7fcfc6;
  }
  .label--dark .note-box { border-color: #0e6f66; background: rgba(0,0,0,0.35); }
  .vertical {
    position: absolute;
    writing-mode: vertical-rl;
    transform: rotate(180deg);
    white-space: nowrap;
  }
  .directions {
    left: 8px; top: 64px; height: 392px;
    font-size: 14px; color: var(--teal); line-height: 16px;
  }
  .ingredients {
    left: 36px; top: 176px; height: 280px;
    font-size: 6.6px; line-height: 10px; color: var(--ink-soft);
    white-space: normal;
  }
  .rule { position: absolute; top: 40px; height: 416px; width: 2px; background: var(--teal-bright); }
  .rule--left { left: 216px; background: var(--teal); width: 1px; }
  .rule--right { left: 232px; }
  .claim {
    left: 216px; top: 42px; height: 414px;
    font-size: 15.5px; line-height: 16px; color: var(--teal);
  }
  .watermark-word {
    left: 236px; top: 36px; height: 424px;
    font-family: "Poppins", Arial, sans-serif; font-weight: 600;
    font-size: 92px; line-height: 78px; color: var(--teal-pale);
    text-align: end;
  }
  .label--dark .watermark-word { color: rgba(0,150,138,0.35); }
  .brand {
    position: absolute; left: 290px; top: 50px; width: 170px;
    text-align: center;
  }
  .brand__dot {
    display: block; width: 46px; height: 46px; margin: 0 auto 8px;
    border-radius: 50%; background: var(--teal-bright);
  }
  .brand__name {
    font-size: 20px; line-height: 22px; color: var(--teal-bright);
  }
  .product-name {
    position: absolute; left: 276px; top: 170px;
    font-family: "Poppins", Arial, sans-serif; font-weight: 600;
    font-size: 43px; color: var(--teal-deep); letter-spacing: -0.5px;
  }
  .label--dark .product-name { color: var(--teal); }
  .product-type {
    position: absolute; left: 318px; top: 208px;
    font-family: "Great Vibes", cursive; font-size: 78px; color: var(--teal-deep);
  }
  .label--dark .product-type { color: var(--teal); }
  .drop { position: absolute; left: 360px; top: 376px; width: 30px; height: 42px; }
  .usage {
    position: absolute; left: 310px; top: 424px; width: 130px;
    text-align: center; font-size: 18px; line-height: 19px; color: var(--teal-deep);
  }
  .label--dark .usage { color: var(--teal); }
</style>
</head>
<body>

  <section class="label label--light" aria-label="Cleanser Gel label, light version">
    <div class="pattern" role="img" aria-label="Faint layered floral mandala background pattern"></div>
    <div class="band band--top"><span class="tagline">Inner Peace - Outer Beauty</span></div>
    <div class="note-box"></div>
    <p class="vertical directions">Directions: Massage onto dry skin for 1-2 minutes - rinse off.</p>
    <p class="vertical watermark-word">Cleanser</p>
    <span class="rule rule--right"></span>
    <p class="vertical claim">Nourishing oil blend melts away make-up and impurities</p>
    <div class="brand">
      <span class="brand__dot"></span>
      <p class="brand__name">Fernlight Skin Care</p>
    </div>
    <h1 class="product-name">Cleanser</h1>
    <p class="product-type">Gel</p>
    <svg class="drop" viewBox="0 0 30 42" aria-hidden="true"><path d="M15 2 C11 12 3 20 3 28 a12 12 0 0 0 24 0 C27 20 19 12 15 2 Z" fill="none" stroke="var(--teal-bright)" stroke-width="2.5"/></svg>
    <p class="usage">1 AM/PM<br>118 mL</p>
    <div class="band band--bottom"></div>
  </section>

  <section class="label label--dark" aria-label="Cleanser Gel label, dark version">
    <div class="pattern" role="img" aria-label="Translucent layered floral mandala background pattern"></div>
    <div class="band band--top"><span class="tagline">Inner Peace - Outer Beauty</span></div>
    <div class="note-box"></div>
    <p class="vertical directions">Directions: Massage onto dry skin for 1-2 minutes - rinse off.</p>
    <p class="vertical ingredients">Ingredients: Water (Aqua), Sodium Laureth Sulfate, Mentha Piperita (Peppermint) Leaf Water, Sodium Lauroyl Oat Amino Acids, Acrylates Copolymer, Cananga Odorata Flower Oil, Melaleuca Alternifolia (Tea Tree) Leaf Oil, Hamamelis Extract, Fragrance (Parfum), Propylene Glycol, Tetrasodium EDTA, Phenoxyethanol, Ethylparaben, Butylparaben, Propylparaben, Methylparaben.</p>
    <p class="vertical watermark-word">Cleanser</p>
    <span class="rule rule--left"></span>
    <span class="rule rule--right"></span>
    <p class="vertical claim">Nourishing oil blend melts away make-up and impurities</p>
    <div class="brand">
      <span class="brand__dot"></span>
      <p class="brand__name">Fernlight Skin Care</p>
    </div>
    <h1 class="product-name">Cleanser</h1>
    <p class="product-type">Gel</p>
    <svg class="drop" viewBox="0 0 30 42" aria-hidden="true"><path d="M15 2 C11 12 3 20 3 28 a12 12 0 0 0 24 0 C27 20 19 12 15 2 Z" fill="none" stroke="var(--teal-bright)" stroke-width="2.5"/></svg>
    <p class="usage">1 AM/PM<br>118 mL</p>
    <div class="band band--bottom"></div>
  </section>

</body>
</html>
```